Concierge Crestline / Medical Supply Ordering Business - Sleek, Efficient, Professional, Elite

www.brixtonfaymedical.example - example website.

We are a concierge supply ordering business for medical and dental that provide DSO price savings on supplies while maintaining business autonomy and independence.

We want a very simple website that looks very professional says what we do and gives a very simple method to contact us & sign up as above.

Target Market(s)

Independent Crestline and Medical Practices

Industry/Entity Type

Crestline and Medical - healthcare

Coding

Coded - Design and coding required

Number of Pages Required

3 page

Font styles to use
Sans Serif

Colors
0054AA
0677BA
7BADD7
CADEEF
E8F1F8

Requirements
Must have
• Simple contact page, sleek efficient design, uncomplicated.
Nice to have
• Sign up page vs just a contact page.
Should not have
• Lots of pages, hard to navigate,

```html
<!DOCTYPE html>
<html lang="en">
<head>
<meta charset="utf-8">
<title>Crestline Dental Supply — Concierge Supply Ordering</title>
<link rel="stylesheet" href="https://fonts.googleapis.com/css2?family=Lato:ital,wght@0,400;0,700;1,400&family=Ubuntu:wght@500;700&display=swap">
<style>
:root{
  --navy:#14264a;
  --ink:#1d2b45;
  --text:#5b6474;
  --accent:#1ea3c8;
  --blue:#0677BA;
  --deep:#0054AA;
  --sky:#7BADD7;
  --pale:#CADEEF;
  --mist:#E8F1F8;
  --grey:#f4f5f7;
  --footer:#101733;
  --footbar:#1c2340;
  --star:#c8103e;
}
*{box-sizing:border-box;margin:0;padding:0}
html,body{width:1200px;height:5220px;overflow:hidden}
body{font-family:"Lato",sans-serif;color:var(--text);background:#fff;position:relative}
h1,h2,h3,h4{font-family:"Ubuntu",sans-serif;color:var(--ink)}
.abs{position:absolute}
section,header,footer{position:absolute;left:0;width:1200px}

/* header */
.site-header{top:0;height:126px;background:#fff;z-index:3}
.contact-chip{position:absolute;top:22px;display:flex;align-items:center;gap:10px;font-size:11px;color:var(--ink)}
.contact-chip b{display:block;font-size:12px}
.contact-chip .dot{width:28px;height:28px;border-radius:50%;background:var(--accent);display:flex;align-items:center;justify-content:center}
.book-btn{position:absolute;left:880px;top:16px;width:182px;height:38px;border-radius:20px;background:var(--accent);color:#fff;font-size:11px;font-weight:700;display:flex;align-items:center;justify-content:center;letter-spacing:.5px}
.rule{position:absolute;top:70px;height:1px;background:#dcdfe4}
.nav a{position:absolute;top:90px;font-size:12px;color:var(--ink);text-decoration:none}
.brand{position:absolute;left:535px;top:0;width:130px;height:150px;background:#fff;border-radius:0 0 40px 40px;display:flex;flex-direction:column;align-items:center;justify-content:center;gap:8px}
.brand .mark{width:54px;height:54px;background:var(--blue);border-radius:6px}
.brand span{font-family:"Ubuntu",sans-serif;font-weight:700;font-size:14px;color:var(--blue)}

/* hero */
.hero{top:126px;height:762px;background:linear-gradient(100deg,#2d3644 0%,#4b5563 45%,#6e7684 70%,#3c4654 100%)}
.hero .kicker{position:absolute;left:106px;top:244px;color:#fff;font-family:"Ubuntu",sans-serif;font-size:19px;letter-spacing:6px}
.hero h1{position:absolute;left:100px;top:270px;color:#fff;font-size:66px;letter-spacing:1px}
.hero .bar{position:absolute;left:104px;top:360px;width:600px;height:3px;background:var(--accent)}
.hero p{position:absolute;left:104px;top:382px;width:620px;color:#fff;font-size:15px;line-height:28px}
.btn{position:absolute;height:40px;border-radius:20px;color:#fff;font-size:13px;font-weight:700;display:flex;align-items:center;justify-content:center;letter-spacing:.5px}
.btn.teal{background:var(--accent)}
.btn.dark{background:#0b0f18}

/* features */
.feature{position:absolute;top:805px;width:318px;height:282px;background:#fff;border-radius:6px;box-shadow:0 6px 24px rgba(0,0,0,.08);text-align:center;padding-top:36px}
.feature h3{font-size:18px;margin:20px 0 14px}
.feature p{font-size:13px;line-height:26px;padding:0 40px}
.icon-bub{width:62px;height:62px;margin:0 auto;border-radius:50%;background:var(--mist);display:flex;align-items:center;justify-content:center}

/* about */
.eyebrow{font-size:11px;font-weight:700;letter-spacing:.5px;color:var(--blue);text-transform:uppercase}
.about{top:1160px;height:470px}
.about h2{position:absolute;left:100px;top:42px;font-size:34px;line-height:52px}
.about p{position:absolute;left:100px;top:156px;width:420px;font-size:13px;line-height:25.5px}
.img-fill{border-radius:8px}
.primary-btn{position:absolute;height:46px;background:var(--accent);color:#fff;font-weight:700;font-size:15px;display:flex;align-items:center;justify-content:center;gap:12px;border-radius:2px}

/* services */
.services{top:1665px;height:655px;background:var(--grey)}
.sec-head{position:absolute;left:0;width:1200px;text-align:center}
.sec-head .eyebrow{display:block;margin-bottom:12px}
.sec-head h2{font-size:35px;margin-bottom:24px}
.sec-head p{width:580px;margin:0 auto;font-size:13px;line-height:25px}
.service{position:absolute;top:263px;width:320px;height:285px;border-radius:6px}
.service .label{position:absolute;bottom:-22px;left:50%;transform:translateX(-50%);background:#fff;padding:12px 16px;font-family:"Ubuntu",sans-serif;font-weight:700;font-size:18px;color:var(--ink);white-space:nowrap;box-shadow:0 4px 14px rgba(0,0,0,.08)}

/* cta band */
.cta{top:2320px;height:308px;background:linear-gradient(90deg,#1c1a1a,#2e2b2a 50%,#1e1c1c)}
.cta h2{position:absolute;top:112px;width:1200px;text-align:center;color:#fff;font-weight:500;font-size:33px;line-height:40px}
.cta h2 em{font-style:normal;color:var(--accent)}
.contact-bar{position:absolute;left:347px;top:2597px;width:502px;height:54px;background:#fff;box-shadow:0 4px 14px rgba(0,0,0,.08);display:flex;align-items:center;justify-content:space-around;font-size:15px;color:var(--ink);z-index:2}

/* testimonials */
.offer{top:2651px;height:645px;background:var(--grey)}
.review{position:absolute;top:250px;width:320px;height:262px;background:#fff;text-align:center;padding-top:66px}
.avatar{position:absolute;top:-30px;left:126px;width:68px;height:68px;border-radius:50%;background:linear-gradient(#8b95a5,#3e4756);border:4px solid #fff}
.stars{color:var(--star);font-size:20px;letter-spacing:6px}
.review p{font-size:13px;line-height:25px;padding:0 50px;margin-top:16px}
.quote{position:absolute;left:136px;bottom:-24px;width:48px;height:48px;border-radius:50%;background:var(--accent);display:flex;align-items:center;justify-content:center;color:#fff;font:700 26px "Ubuntu",sans-serif}
.who{position:absolute;top:553px;width:320px;text-align:center}
.who b{display:block;font-family:"Ubuntu",sans-serif;font-size:17px;color:var(--ink);margin-bottom:6px}
.who span{font-size:13px}

/* why */
.why{top:3296px;height:608px;background:linear-gradient(100deg,#3e4a60 0%,#5d6578 45%,#3a3330 70%,#5a4a3e 100%)}
.why-card{position:absolute;left:90px;top:70px;width:496px;height:466px;background:#fff;border-radius:6px;padding:56px 50px}
.why-card h2{font-size:35px;margin:10px 0 28px}
.why-item{display:flex;gap:22px;margin-bottom:28px}
.why-item svg{flex:none;margin-top:8px}
.why-item h4{font-family:"Lato",sans-serif;color:var(--blue);font-size:13px;margin-bottom:6px}
.why-item p{font-size:13px;line-height:25px}

/* contact */
.contact{top:3904px;height:758px;background:#fff}
.form-card{position:absolute;left:140px;top:218px;width:912px;height:500px;background:#fff;box-shadow:0 4px 30px rgba(0,0,0,.07);border-radius:6px}
.field{position:absolute;height:40px;border:2px solid var(--blue);border-radius:20px;padding:0 34px;display:flex;align-items:center;font-style:italic;font-size:12px;color:#7a8492}
.field.active{background:var(--mist)}
.field label{position:absolute;left:30px;top:-9px;background:#fff;padding:0 6px;font-style:normal;font-size:12px;color:var(--ink)}
.field.active label{color:var(--blue);background:linear-gradient(#fff 50%,var(--mist) 50%)}
.field.area{height:150px;border-radius:14px;align-items:flex-start;padding-top:20px}
.circle{position:absolute;width:30px;height:30px;border-radius:50%;border:2px solid var(--blue)}
.submit{position:absolute;left:700px;top:416px;width:144px;height:40px;border-radius:20px;background:var(--accent);color:#fff;font-size:12px;font-weight:700;display:flex;align-items:center;justify-content:flex-end;padding-right:10px;gap:14px}
.submit i{width:26px;height:26px;border-radius:50%;background:#fff;display:block}

/* footer */
.site-footer{top:4662px;height:503px;background:var(--footer)}
.sq{position:absolute;top:106px;width:38px;height:38px;background:#2a3a78}
.foot-brand{position:absolute;left:500px;top:44px;width:200px;text-align:center}
.foot-brand .mark{width:78px;height:78px;margin:0 auto 12px;background:var(--blue);border-radius:6px}
.foot-brand span{font-family:"Ubuntu",sans-serif;font-weight:700;font-size:14px;color:#fff}
.back-top{position:absolute;left:972px;top:106px;display:flex;align-items:center;gap:16px;color:#fff;font-weight:700;font-size:14px}
.back-top i{width:42px;height:42px;background:var(--sky);display:flex;align-items:center;justify-content:center}
.site-footer h3{position:absolute;top:249px;width:1200px;text-align:center;color:#fff;font-size:27px}
.site-footer .intro{position:absolute;top:302px;left:310px;width:580px;text-align:center;color:#dfe3ee;font-size:15px;line-height:26px}
.info{position:absolute;top:404px;display:flex;align-items:center;gap:16px;color:#fff}
.info small{display:block;font-size:14px;color:#c9cfdd}
.info b{font-size:15px}
.footbar{top:5165px;height:55px;background:var(--footbar);color:#fff;font-size:13px}
.footbar span{position:absolute;top:20px}
</style>
</head>
<body>

<header class="site-header">
  <div class="contact-chip" style="left:122px">
    <div class="dot"><svg width="14" height="14" viewBox="0 0 24 24"><path d="M6 3l3 4-2 2c1 3 4 6 7 7l2-2 4 3-2 4C10 21 3 14 3 5z" fill="#fff"/></svg></div>
    <div><b>Call Us:</b>(555) 014-2290</div>
  </div>
  <div class="contact-chip" style="left:280px">
    <div class="dot"><svg width="14" height="14" viewBox="0 0 24 24"><rect x="3" y="6" width="18" height="12" fill="none" stroke="#fff" stroke-width="2"/><path d="M3 6l9 7 9-7" fill="none" stroke="#fff" stroke-width="2"/></svg></div>
    <div><b>Email:</b>office@crestlinedental.example</div>
  </div>
  <div class="book-btn">BOOK APPOINTMENT</div>
  <div class="rule" style="left:122px;width:362px"></div>
  <div class="rule" style="left:700px;width:364px"></div>
  <nav class="nav">
    <a style="left:125px">Home</a><a style="left:236px">About Us</a><a style="left:388px">Services</a>
    <a style="left:706px">Testimonials</a><a style="left:881px">Contact Us</a>
  </nav>
  <div class="brand"><div class="mark"></div><span>Crestline</span></div>
</header>

<section class="hero" role="img" aria-label="Office team reviewing supply orders on a tablet">
  <div class="kicker">EXPERTS IN</div>
  <h1>SUPPLY ORDERING</h1>
  <div class="bar"></div>
  <p>Lorem ipsum dolor sit amet, consectetur adipiscing elit, sed do eiusmod tempor ididunt ut labore et dolore magna aliqua</p>
  <div class="btn teal" style="left:106px;top:470px;width:146px">LEARN MORE</div>
  <div class="btn dark" style="left:268px;top:470px;width:174px">REQUEST QUOTE</div>
</section>

<div class="feature" style="left:93px">
  <div class="icon-bub"><svg width="40" height="40" viewBox="0 0 40 40" fill="none" stroke="#0677BA" stroke-width="2"><circle cx="20" cy="20" r="12"/><circle cx="20" cy="20" r="4"/><path d="M20 4v10M20 26v10M4 20h10M26 20h10"/></svg></div>
  <h3>Global Reach</h3><p>Lorem ipsum dolor sit amet, consect adipiscing elit, sed do eiusmod tempor incididunt ut labore et dolore</p>
</div>
<div class="feature" style="left:443px">
  <div class="icon-bub"><svg width="40" height="40" viewBox="0 0 40 40" fill="none" stroke="#0677BA" stroke-width="2"><rect x="9" y="14" width="22" height="16" rx="2"/><path d="M15 14v-4h10v4M9 21h22"/></svg></div>
  <h3>Professionalism</h3><p>Lorem ipsum dolor sit amet, consect adipiscing elit, sed do eiusmod tempor incididunt ut labore et dolore</p>
</div>
<div class="feature" style="left:788px">
  <div class="icon-bub"><svg width="40" height="40" viewBox="0 0 40 40" fill="none" stroke="#0677BA" stroke-width="2"><path d="M20 7l4 9 9 1-7 6 2 9-8-5-8 5 2-9-7-6 9-1z"/></svg></div>
  <h3>Great Reviews</h3><p>Lorem ipsum dolor sit amet, consect adipiscing elit, sed do eiusmod tempor incididunt ut labore et dolore</p>
</div>

<section class="about">
  <div class="eyebrow abs" style="left:101px;top:24px">See the difference —</div>
  <h2>Advanced Supply<br>Ordering Services</h2>
  <p>Lorem ipsum dolor sit amet, consectetur adipiscing elit, sed do eius mod tempor incididunt ut labore et dolore magna aliqua. Ut enim ad minim veniam, quis nostrud exercitation ullamco laboris nisi ut aliquip ex ea commodo consequat. Duis aute irure dolor in Lorem ipsum dolor sit amet, consectetur adipiscing elit, sed do eius mod tempor incididunt ut labore et dolore magna aliqua. Ut enim ad minim veniam, quis nostrud exercitation ullamco laboris nisi ut aliquip ex ea commodo consequat. Duis aute irure dolor in</p>
  <div class="primary-btn" style="left:101px;top:384px;width:156px">Contact us <svg width="18" height="12" viewBox="0 0 18 12" fill="none" stroke="#fff" stroke-width="2"><path d="M1 6h15M11 1l5 5-5 5"/></svg></div>
  <svg class="abs" style="left:534px;top:120px" width="130" height="180" viewBox="0 0 130 180" fill="none"><path d="M90 10A80 80 0 0 0 90 170" stroke="#CADEEF" stroke-width="2" stroke-dasharray="4 5"/><path d="M92 40A50 50 0 0 0 92 140" stroke="#7BADD7" stroke-width="2"/><circle cx="80" cy="90" r="24" fill="#fff" stroke="#E8F1F8" stroke-width="6"/><rect x="70" y="80" width="20" height="20" rx="3" fill="#0677BA"/></svg>
  <div class="abs img-fill" style="left:608px;top:25px;width:497px;height:407px;background:linear-gradient(135deg,#e4e6ea,#c2c7cf 55%,#7c8390)" role="img" aria-label="Professional holding a tablet in a bright office"></div>
</section>

<section class="services">
  <div class="sec-head" style="top:88px">
    <span class="eyebrow">— Our services —</span>
    <h2>Services We Offer</h2>
    <p>Lorem ipsum dolor sit amet, consectetur adipiscing elit, sed do eiusmod tempor incididunt ut labore et dolore magna aliqua. Ut enim ad minim veniam, quis nostrud exercitation</p>
  </div>
  <div class="service" style="left:93px;background:linear-gradient(135deg,#6c7a8c,#2f3a4c)" role="img" aria-label="Business partners shaking hands"><span class="label">Order Fulfillment</span></div>
  <div class="service" style="left:441px;background:linear-gradient(135deg,#c9ccd2,#6a707c)" role="img" aria-label="Colleagues reviewing pricing on a laptop"><span class="label">Price Savings</span></div>
  <div class="service" style="left:788px;background:linear-gradient(135deg,#5b5f68,#2a2d34)" role="img" aria-label="Team working at a desk with a tablet"><span class="label">Timely Delivery</span></div>
</section>

<section class="cta" role="img" aria-label="Dark office background">
  <h2>We're On <em>Call 24/7</em> to React Promptly to Your<br>Supply Ordering Needs</h2>
</section>
<div class="contact-bar"><span>+ (555) 010-4477</span><span>[or]</span><span>orders@crestlinedental.example</span></div>

<section class="offer">
  <div class="sec-head" style="top:37px">
    <span class="eyebrow">— Our services —</span>
    <h2>What we can offer you</h2>
    <p>Lorem ipsum dolor sit amet, consectetur adipiscing elit, sed do eiusmod tempor incididunt ut labore et dolore magna aliqua. Ut enim ad minim veniam, quis nostrud exercitation</p>
  </div>
  <div class="review" style="left:93px"><div class="avatar" role="img" aria-label="Client portrait"></div><div class="stars">★★★★★</div><p>Lorem ipsum dolor sit amet, consectetur adipiscing elit, sed do eiusmod tempor incididunt ut labore et dolore</p><div class="quote">“</div></div>
  <div class="review" style="left:441px"><div class="avatar" role="img" aria-label="Client portrait"></div><div class="stars">★★★★★</div><p>Lorem ipsum dolor sit amet, consectetur adipiscing elit, sed do eiusmod tempor incididunt ut labore et dolore</p><div class="quote">“</div></div>
  <div class="review" style="left:788px"><div class="avatar" role="img" aria-label="Client portrait"></div><div class="stars">★★★★★</div><p>Lorem ipsum dolor sit amet, consectetur adipiscing elit, sed do eiusmod tempor incididunt ut labore et dolore</p><div class="quote">“</div></div>
  <div class="who" style="left:93px"><b>Dana Whitfield</b><span>Los Angeles</span></div>
  <div class="who" style="left:441px"><b>Dana Whitfield</b><span>Los Angeles</span></div>
  <div class="who" style="left:788px"><b>Dana Whitfield</b><span>Los Angeles</span></div>
</section>

<section class="why" role="img" aria-label="Team meeting around a table in an office">
  <div class="why-card">
    <span class="eyebrow">See the difference —</span>
    <h2>Why Choose Us?</h2>
    <div class="why-item"><svg width="34" height="34" viewBox="0 0 34 34" fill="none" stroke="#0677BA" stroke-width="2"><circle cx="17" cy="11" r="6"/><path d="M6 30c0-7 5-11 11-11s11 4 11 11z"/></svg><div><h4>Customer Support</h4><p>Lorem ipsum dolor sit amet, consectetur adipiscing elit, sed do eiusmod tempor incididunt ut labore et</p></div></div>
    <div class="why-item"><svg width="34" height="34" viewBox="0 0 34 34" fill="none" stroke="#0677BA" stroke-width="2"><path d="M17 4l4 8 9 1-7 6 2 9-8-5-8 5 2-9-7-6 9-1z"/></svg><div><h4>Efficient Ordering</h4><p>Lorem ipsum dolor sit amet, consectetur adipiscing elit, sed do eiusmod tempor incididunt ut labore et</p></div></div>
    <div class="why-item"><svg width="34" height="34" viewBox="0 0 34 34" fill="none" stroke="#0677BA" stroke-width="2"><path d="M6 22v-5a11 11 0 0 1 22 0v5"/><rect x="4" y="20" width="6" height="9" rx="2"/><rect x="24" y="20" width="6" height="9" rx="2"/></svg><div><h4>Regulatory Compliance</h4><p>Lorem ipsum dolor sit amet, consectetur adipiscing elit, sed do eiusmod tempor incididunt ut labore et</p></div></div>
  </div>
</section>

<section class="contact">
  <div class="sec-head" style="top:48px">
    <span class="eyebrow">— Contact us —</span>
    <h2>Get In Touch With Us</h2>
    <p>Lorem ipsum dolor sit amet, consectetur adipiscing elit, sed do eiusmod tempor incididunt ut labore et dolore magna aliqua. Ut enim ad minim veniam, quis nostrud exercitation</p>
  </div>
  <div class="form-card">
    <div class="field active" style="left:52px;top:60px;width:392px"><label>Your Name</label>John</div>
    <div class="field" style="left:466px;top:60px;width:392px"><label>Your Website</label>www.brixtonfaymedical.example</div>
    <div class="field" style="left:52px;top:134px;width:392px"><label>Your Phone</label>123 456 789</div>
    <div class="field" style="left:466px;top:134px;width:392px"><label>Your Email</label>info@yourpractice.example</div>
    <div class="field area" style="left:52px;top:210px;width:806px"><label>Your Message</label>Type Message</div>
    <div class="circle" style="left:66px;top:421px"></div>
    <div class="circle" style="left:105px;top:421px"></div>
    <div class="circle" style="left:144px;top:421px"></div>
    <div class="circle" style="left:183px;top:421px"></div>
    <div class="submit">Submit Now <i></i></div>
  </div>
</section>

<footer class="site-footer">
  <div class="sq" style="left:86px"></div><div class="sq" style="left:136px"></div><div class="sq" style="left:186px"></div><div class="sq" style="left:236px"></div>
  <div class="foot-brand"><div class="mark"></div><span>Crestline Dental Supply</span></div>
  <div class="back-top">Back to top <i><svg width="16" height="10" viewBox="0 0 16 10" fill="none" stroke="#fff" stroke-width="2.5"><path d="M2 8l6-6 6 6"/></svg></i></div>
  <h3>Get free assessment today</h3>
  <p class="intro">Lorem ipsum dolor sit amet, consectetur adipiscing elit, sed do eiusmod tempor incididunt ut labore et dolore magna aliqua.</p>
  <div class="info" style="left:218px"><svg width="50" height="50" viewBox="0 0 50 50" fill="none" stroke="#1ea3c8" stroke-width="2"><path d="M12 6l8 10-5 5c3 6 8 11 14 14l5-5 10 8-5 8C22 44 6 28 6 11z"/></svg><div><small>Make a Call</small><b>+1-555-014-2290</b></div></div>
  <div class="info" style="left:476px"><svg width="50" height="50" viewBox="0 0 50 50" fill="none" stroke="#1ea3c8" stroke-width="2"><rect x="5" y="12" width="40" height="28"/><path d="M5 12l20 16 20-16"/></svg><div><small>Mail Us On</small><b>hello@crestlinedental.example</b></div></div>
  <div class="info" style="left:756px"><svg width="50" height="50" viewBox="0 0 50 50" fill="none" stroke="#1ea3c8" stroke-width="2"><path d="M25 44S12 28 12 19a13 13 0 0 1 26 0c0 9-13 25-13 25z"/><circle cx="25" cy="19" r="5"/></svg><div><small>Location</small><b>48 Harbor Mill Rd</b></div></div>
</footer>
<div class="footbar abs" style="left:0;width:1200px">
  <span style="left:86px">Crestline Dental Supply</span>
  <span style="left:803px">Privacy Policy</span>
  <span style="left:915px">Terms &amp; Conditions</span>
  <span style="left:1056px">Site Map</span>
</div>

</body>
</html>
```